SOCIAL MEDIA MARKETING CAMPAIGN FOR TELQAVISION.COM

please go through below details & also find the attachments of OUR PREVIOUS brindle ads.
https://help.brindleads.example/promopolicy/item/482913?hl=en-AU
Create an ad for each business line.
PRINT, WEB, EVENT, EXHIBIT & GIFTS
The explanation below is only indicative of what each business line
consists of and should not be included in the ad.
------------------------------------------
PRINT:
Corporate Identity
Logo Creation
Annual Reports
Interactive Brochures,
Catalogs,
Presentations & Press Kits
Web:
Domain Registration
Database Integration
Web Design / Hosting
Intranet Design
Programming
Search Engine Optimization
Multimedia Presentations
Corporate Documentaries
Corporate and Safety Videos
Event:
Site Selection & Contract
Audio Visuals
VIP Handling
Online Registration
Exhibit:
Design & Construction
3D Visualization
In-house Fabrication
Transport / Storages
Trade show Gifts
Business Gifts & Premiums:
Custom Design Gifts
Employee Recognition
Sourcing Limited Editions
Ad sizes :
Mobile leaderboard: 320 x 50 pixels
Banner: 468 x 60 pixels
Leaderboard: 728 x 90 pixels
Square: 250 x 250 pixels
Small square: 200 x 200 pixels
Large rectangle: 336 x 280 pixels
Inline rectangle: 300 x 250 pixels
Skyscraper: 120 x 600 pixels
Wide skyscraper: 160 x 600 pixels
Half-page: 300 x 600 pixels
http://www.thelookupkiosk.example/how-to-promote-your-business-using-brindle-banner-grid
More details please go through: telqavision.com
Target Market(s)
Middle east
Industry/Entity Type
Marketing
Look and feel

```html
<!DOCTYPE html>
<html lang="en">
<head>
<meta charset="utf-8">
<title>Telqavision display ad set</title>
<link href="https://fonts.googleapis.com/css2?family=Open+Sans:wght@400;600;700&family=Signika:wght@500;600&display=swap" rel="stylesheet">
<style>
  :root {
    --page: #ffffff;
    --ink: #1a1a1a;
    --dark: #0c0f10;
    --teal: #2c4b4b;
    --white: #ffffff;
    --brand: #e4572a;
    --design: #e2d23e;
    --events: #e2416b;
    --events-soft: #f0728c;
    --web: #1c9fd8;
    --expo: #1f8fca;
    --expo-deep: #1565a8;
    --gifts: #f5a623;
  }
  * { margin: 0; padding: 0; box-sizing: border-box; }
  html, body { width: 1200px; height: 1000px; overflow: hidden; background: var(--page); }
  body { position: relative; font-family: "Open Sans", Arial, sans-serif; color: var(--white); }

  .size-label { position: absolute; color: var(--ink); font-size: 19px; line-height: 25px; font-weight: 400; }

  .ad { position: absolute; overflow: hidden; }
  .panel { position: absolute; left: 0; width: 100%; }
  .panel--dark-to-teal { background: linear-gradient(90deg, var(--dark) 0%, #151c1d 55%, var(--teal) 100%); }
  .panel--teal-to-dark { background: linear-gradient(90deg, var(--teal) 0%, #1a2a2b 45%, var(--dark) 100%); }

  .t { position: absolute; white-space: nowrap; }
  .headline { font-family: "Signika", Arial, sans-serif; font-weight: 600; line-height: 1; letter-spacing: 0.5px; }
  .strap { font-weight: 700; line-height: 1; }
  .service { font-weight: 700; line-height: 1; }
  .items { font-weight: 600; line-height: 1.3; }
  .dot { color: var(--accent); padding: 0 2px; }
  .rule { position: absolute; height: 2px; }

  .brand-name { position: absolute; font-family: "Open Sans", Arial, sans-serif; font-weight: 700; color: var(--brand); line-height: 1; letter-spacing: -0.5px; }
  .tagline { font-weight: 700; line-height: 1; }
  .contact { font-weight: 600; line-height: 1.35; }

  .art { position: absolute; border-radius: 8px; }

  .ad--banner { left: 410px; top: 146px; width: 468px; height: 60px; --accent: var(--design); }
  .ad--square { left: 246px; top: 300px; width: 250px; height: 250px; --accent: var(--events); }
  .ad--small { left: 561px; top: 345px; width: 200px; height: 200px; --accent: var(--web); }
  .ad--large { left: 362px; top: 633px; width: 336px; height: 280px; --accent: var(--expo); }
  .ad--sky { left: 847px; top: 303px; width: 160px; height: 600px; --accent: var(--gifts); }
</style>
</head>
<body>

  <div class="size-label" style="left:551px; top:115px;">banner: 468 x 60px</div>
  <div class="size-label" style="left:276px; top:271px;">square: 250 x 250px</div>
  <div class="size-label" style="left:592px; top:294px;">small square:<br>200 x 200px</div>
  <div class="size-label" style="left:846px; top:246px;">WIDE skyscraper:<br>160 x 600px</div>
  <div class="size-label" style="left:394px; top:600px;">large rectangle: 336 x 280px</div>

  <!-- Banner 468 x 60 -->
  <section class="ad ad--banner">
    <div class="panel panel--dark-to-teal" style="top:0; width:234px; height:60px;"></div>
    <div class="panel panel--teal-to-dark" style="top:0; left:234px; width:234px; height:60px;"></div>
    <div class="t headline" style="left:7px; top:7px; font-size:16.5px; color:var(--design);">DESIGN</div>
    <div class="t strap" style="left:68px; top:11px; font-size:8px;">EMPOWERS BUSINESS</div>
    <div class="t service" style="left:7px; top:31px; font-size:6.5px; color:var(--design);">Turnkey Event Management</div>
    <div class="t items" style="left:7px; top:40px; font-size:5px;">Logo Design<span class="dot">•</span>Brochures<span class="dot">•</span>Annual Reports</div>
    <div class="rule" style="left:5px; top:51px; width:218px; background:var(--design);"></div>
    <div class="art" role="img" aria-label="Yellow line icon of a pencil" style="left:185px; top:4px; width:34px; height:44px; background:linear-gradient(135deg, rgba(226,210,62,0.35), rgba(226,210,62,0.1));"></div>
    <div class="brand-name" style="left:258px; top:14px; font-size:19px;">telqa</div>
    <div class="t tagline" style="left:258px; top:39px; font-size:6px;">we design your success</div>
    <div class="t contact" style="left:357px; top:14px; font-size:5.5px;">Bahrain: +973.1555.0147<br>Saudi Arabia: +9661.3555.0286</div>
    <div class="t contact" style="left:357px; top:38px; font-size:5.5px;">telqavision.com</div>
  </section>

  <!-- Square 250 x 250 -->
  <section class="ad ad--square">
    <div class="panel panel--teal-to-dark" style="top:0; height:150px;"></div>
    <div class="panel panel--dark-to-teal" style="top:150px; height:100px;"></div>
    <div class="t headline" style="left:12px; top:40px; font-size:17px; line-height:18px; color:var(--events-soft);">CORPORATE<br>EVENTS</div>
    <div class="t strap" style="left:12px; top:75px; font-size:8px;">EMPOWERS BUSINESS</div>
    <div class="rule" style="left:12px; top:88px; width:118px; background:var(--events);"></div>
    <div class="art" role="img" aria-label="Pink line icon of a spiral eye" style="left:125px; top:28px; width:115px; height:70px; background:linear-gradient(90deg, rgba(226,65,107,0.4), rgba(240,114,140,0.12));"></div>
    <div class="t service" style="left:12px; top:95px; font-size:6px; color:var(--events);">Turnkey Event Management</div>
    <div class="t items" style="left:12px; top:104px; font-size:5px;">Concept<span class="dot">•</span>Execution<span class="dot">•</span>AV<span class="dot">•</span><br>Video<span class="dot">•</span>Presentations</div>
    <div class="brand-name" style="left:14px; top:180px; font-size:21px;">telqa</div>
    <div class="t tagline" style="left:14px; top:210px; font-size:8px;">we make it memorable</div>
    <div class="t contact" style="left:133px; top:187px; font-size:5.5px;">Bahrain: +973.1555.0147<br>Saudi Arabia: +9661.3555.0286</div>
    <div class="t contact" style="left:133px; top:211px; font-size:5.5px;">telqavision.com</div>
  </section>

  <!-- Small square 200 x 200 -->
  <section class="ad ad--small">
    <div class="panel panel--teal-to-dark" style="top:0; height:100px;"></div>
    <div class="panel panel--dark-to-teal" style="top:100px; height:100px;"></div>
    <div class="t headline" style="left:10px; top:28px; font-size:15px; color:var(--web);">WEBSITE</div>
    <div class="t strap" style="left:10px; top:45px; font-size:7.5px;">EMPOWERS BUSINESS</div>
    <div class="rule" style="left:8px; top:67px; width:172px; background:var(--web);"></div>
    <div class="art" role="img" aria-label="Blue line icon of a globe with an upward arrow" style="left:125px; top:4px; width:68px; height:62px; background:linear-gradient(135deg, rgba(28,159,216,0.4), rgba(28,159,216,0.1));"></div>
    <div class="t service" style="left:10px; top:74px; font-size:5.5px; color:var(--web);">Web &amp; Multimedia Solution</div>
    <div class="t items" style="left:10px; top:83px; font-size:5px;">Design &amp; Hosting<span class="dot">•</span>Portals<span class="dot">•</span>Interactive Presentations</div>
    <div class="brand-name" style="left:54px; top:120px; font-size:20px;">telqa</div>
    <div class="t tagline" style="left:50px; top:148px; font-size:6.5px;">we web the world for you</div>
    <div class="t contact" style="left:50px; top:167px; font-size:5.5px;">Bahrain: +973.1555.0147<br>Saudi Arabia: +9661.3555.0286<br>telqavision.com</div>
  </section>

  <!-- Large rectangle 336 x 280 -->
  <section class="ad ad--large">
    <div class="panel panel--dark-to-teal" style="top:0; height:170px;"></div>
    <div class="panel panel--teal-to-dark" style="top:170px; height:110px;"></div>
    <div class="t headline" style="left:18px; top:38px; font-size:31px; color:var(--expo);">EXHIBITION</div>
    <div class="t strap" style="left:19px; top:71px; font-size:15.5px;">EMPOWERS BUSINESS</div>
    <div class="art" role="img" aria-label="Blue line icon of two overlapping speech bubbles" style="left:208px; top:25px; width:108px; height:72px; background:linear-gradient(135deg, rgba(31,143,202,0.4), rgba(21,101,168,0.12));"></div>
    <div class="rule" style="left:18px; top:101px; width:228px; height:2.5px; background:linear-gradient(90deg, var(--expo-deep), var(--expo));"></div>
    <div class="t service" style="left:18px; top:116px; font-size:11.5px; color:var(--expo-deep);">Exhibit &amp; Tradeshow Management</div>
    <div class="t items" style="left:18px; top:141px; font-size:10px; font-weight:400;">Design &amp; Fabrication<span class="dot">•</span> 3D Visualization<span class="dot">•</span> Large Format</div>
    <div class="brand-name" style="left:40px; top:205px; font-size:25px;">telqa</div>
    <div class="t tagline" style="left:22px; top:241px; font-size:9px;">we ensure that you get noticed</div>
    <div class="t contact" style="left:195px; top:211px; font-size:7px;">Bahrain: +973.1555.0147<br>Saudi Arabia: +9661.3555.0286</div>
    <div class="t contact" style="left:195px; top:240px; font-size:7px;">telqavision.com</div>
  </section>

  <!-- Wide skyscraper 160 x 600 -->
  <section class="ad ad--sky">
    <div class="panel panel--dark-to-teal" style="top:0; height:422px;"></div>
    <div class="panel panel--teal-to-dark" style="top:422px; height:178px;"></div>
    <div class="art" role="img" aria-label="Orange line icon of a rounded star-shaped gift emblem" style="left:22px; top:20px; width:120px; height:130px; background:linear-gradient(135deg, rgba(245,166,35,0.4), rgba(245,166,35,0.1));"></div>
    <div class="t headline" style="left:14px; top:198px; font-size:23px; line-height:31px; color:var(--gifts);">CORPORATE<br>GIFTS</div>
    <div class="t strap" style="left:16px; top:261px; font-size:10px;">EMPOWERS BUSINESS</div>
    <div class="rule" style="left:16px; top:297px; width:123px; height:3px; background:var(--gifts);"></div>
    <div class="t service" style="left:16px; top:331px; font-size:9.5px; line-height:12px; color:var(--gifts);">B2B Gifts &amp; Premiums<br>Sourcing</div>
    <div class="t items" style="left:16px; top:360px; font-size:8px; font-weight:400; line-height:11px;">Custom Design<span class="dot">•</span> Trophies<span class="dot">•</span><br>Limited Editions</div>
    <div class="brand-name" style="left:22px; top:467px; font-size:22px;">telqa</div>
    <div class="t tagline" style="left:14px; top:502px; font-size:8.5px;">we make sure it's treasured</div>
    <div class="t contact" style="left:15px; top:544px; font-size:7.5px; line-height:10px;">Bahrain: +973.1555.0147<br>Saudi Arabia: +9661.3555.0286<br>telqavision.com</div>
  </section>

</body>
</html>
```